New flyer design for construction company marketing and description of services.

I want to have a flyer design that my techs will carry to deliver after job completion or for marketing purposes, to explain what services we provide, we offer General construction services.

Brellor Homecraft Sevices originated from a family-owned and operated contractor business, performing home renovation, addition, and construction work in the NYC area since 2004.

Today, we specialize in reliable and affordable Construction services for residential and commercial clients In 2014, we expanded to northern New Jersey. In 2016, we brought quality home improvement and repair services to new Bucks County, PA, and nearby New Jersey areas.
We offer carpentry, electrical, plumbing, renovation, remodel, cleaning services and landscaping.
I would like to have a section for home rental maintenance.

Target Market(s)

Homeowners, rental properties, real state and Senior citizen

Industry/Entity Type

Construction Company

Colors

Designer to choose colors to be used in the design.

Requirements
Must have
• A special design that will attract 55 + clients maybe a logo version that will be more attractive to seniors. I would updated the briefing with design and previous pictures, but we have all available in our social media instagram and facebook:
• https://www.pictogram.example/brellorhomecraft/?hl=en
• https://www.friendsbook.example/brellorhome/
Nice to have
• New design ideas and layouts.

```html
<!DOCTYPE html>
<html lang="en">
<head>
<meta charset="utf-8">
<title>Brellor Homecraft Sevices – Flyers</title>
<link rel="stylesheet" href="https://fonts.googleapis.com/css2?family=Russo+One&family=Roboto+Slab:wght@700;800&family=Montserrat:wght@400;600;700&display=swap">
<style>
  :root {
    --red: #e31b23;
    --yellow: #f6c416;
    --black: #141414;
    --charcoal: #2b2b2b;
    --white: #ffffff;
    --ink: #333333;
    --page: #e2e2e2;
    --photo-a: #5a7a4a;
    --photo-b: #2f3d5c;
    --van-a: #8a9a7a;
    --van-b: #1e1e1e;
  }
  * { box-sizing: border-box; margin: 0; padding: 0; }
  html, body { width: 820px; height: 1200px; overflow: hidden; }
  body { background: var(--page); position: relative; font-family: "Montserrat", sans-serif; color: var(--ink); }

  .flyer { position: absolute; left: 20px; width: 780px; height: 560px; background: var(--white); overflow: hidden; box-shadow: 0 2px 8px rgba(0,0,0,.2); }
  .flyer--front { top: 20px; }
  .flyer--back { top: 620px; }

  .hero-frame { position: absolute; left: 36px; top: 58px; width: 420px; height: 400px; z-index: 3; }

  .logo { position: absolute; left: 480px; top: 26px; display: flex; align-items: center; gap: 8px; }
  .logo__mark { width: 26px; height: 26px; background: var(--red); }
  .logo__name { font-family: "Russo One", sans-serif; font-size: 34px; color: var(--black); line-height: 1; }
  .logo__tag { position: absolute; left: 34px; top: 38px; font-size: 7px; letter-spacing: 2px; font-weight: 600; white-space: nowrap; }

  .headline { position: absolute; left: 480px; top: 92px; font-family: "Roboto Slab", serif; font-weight: 800; line-height: 1.05; text-transform: uppercase; white-space: nowrap; }
  .headline__lead { color: var(--red); font-size: 22px; display: block; }
  .headline__main { color: var(--black); font-size: 24px; display: block; }
  .flyer--back .headline__lead, .flyer--back .headline__main { font-size: 15px; }

  .about { position: absolute; left: 480px; top: 152px; width: 290px; font-size: 8.5px; line-height: 1.35; }
  .about p + p { margin-top: 6px; }

  .services { position: absolute; font-size: 9.5px; font-weight: 600; }
  .services__title { color: var(--red); font-weight: 700; font-size: 11px; text-transform: uppercase; margin-bottom: 4px; line-height: 14px; }
  .services__spacer { height: 18px; }
  .services ul { list-style: none; }
  .services li { display: flex; align-items: center; gap: 5px; margin-bottom: 3px; white-space: nowrap; line-height: 11px; }
  .services li::before { content: "✓"; display: inline-flex; align-items: center; justify-content: center; width: 9px; height: 9px; border: 1px solid var(--red); color: var(--red); font-size: 7px; }

  .accent-stripe { position: absolute; left: 420px; top: 340px; width: 360px; height: 8px; background: var(--red); clip-path: polygon(4% 0, 100% 0, 100% 100%, 0 100%); }
  .reviews-band { position: absolute; left: 380px; top: 352px; width: 400px; height: 88px; background: var(--black); clip-path: polygon(11% 0, 100% 0, 100% 100%, 0 100%); }
  .reviews-band__text { position: absolute; left: 56px; top: 12px; font-family: "Russo One", sans-serif; color: var(--white); font-size: 16px; line-height: 1.3; white-space: nowrap; }
  .reviews-band__stars { color: var(--yellow); letter-spacing: 1px; }
  .reviews-band__url { color: var(--red); }
  .follow { position: absolute; right: 16px; bottom: 10px; display: flex; align-items: center; gap: 4px; color: var(--white); font-size: 9px; }
  .follow__icon { width: 13px; height: 13px; background: var(--yellow); }

  .email-strip { position: absolute; left: 340px; top: 446px; width: 440px; height: 34px; background: var(--charcoal); clip-path: polygon(6% 0, 100% 0, 100% 100%, 0 100%); display: flex; align-items: center; padding-left: 60px; gap: 8px; color: var(--white); font-size: 11px; letter-spacing: 1px; }
  .email-strip svg { flex: none; }

  .call-block { position: absolute; left: 0; top: 410px; width: 380px; height: 150px; background: var(--red); clip-path: polygon(0 28%, 72% 0, 100% 100%, 0 100%); z-index: 2; }
  .call-block__text { position: absolute; left: 34px; bottom: 18px; font-family: "Russo One", sans-serif; color: var(--white); line-height: 1; }
  .call-block__label { font-size: 30px; display: block; }
  .call-block__phone { font-size: 36px; display: block; }

  .estimate { position: absolute; left: 664px; top: 244px; width: 82px; height: 82px; }
  .estimate__text { position: absolute; inset: 0; display: flex; align-items: center; justify-content: center; text-align: center; font-family: "Roboto Slab", serif; font-weight: 700; font-size: 11px; line-height: 1.1; color: var(--black); }
</style>
</head>
<body>

<section class="flyer flyer--front">
  <svg class="hero-frame" viewBox="0 0 420 400" role="img" aria-label="Photo: smiling handyman in a blue work shirt and cap holding a clipboard and tool bag">
    <defs>
      <linearGradient id="photoFront" x1="0" y1="0" x2="1" y2="1">
        <stop offset="0" stop-color="var(--photo-a)"/>
        <stop offset="1" stop-color="var(--photo-b)"/>
      </linearGradient>
    </defs>
    <polygon points="105,0 315,0 420,200 315,400 105,400 0,200" fill="var(--red)"/>
    <polygon points="112,12 308,12 406,200 308,388 112,388 14,200" fill="var(--yellow)"/>
    <polygon points="116,18 304,18 399,200 304,382 116,382 21,200" fill="url(#photoFront)"/>
  </svg>

  <div class="logo">
    <span class="logo__mark"></span>
    <span class="logo__name">Brellor</span>
    <span class="logo__tag">HOMECRAFT SERVICES</span>
  </div>

  <h1 class="headline">
    <span class="headline__lead">A better way to</span>
    <span class="headline__main">Get tasks done</span>
  </h1>

  <div class="about">
    <p>Brellor Homecraft Sevices originated from a family-owned and operated contractor business, performing home renovation, addition, and construction work in the NYC area since 2004.</p>
    <p>Today, we specialize in reliable and affordable construction services for residential and commercial clients. In 2014, we expanded to northern New Jersey. In 2016, we brought quality home improvement and repair services to new Bucks County, PA, and nearby New Jersey areas.</p>
  </div>

  <div class="services" style="left:480px; top:280px;">
    <div class="services__title">Our Service</div>
    <ul>
      <li>General Contractor</li>
      <li>Property Maintenance</li>
    </ul>
  </div>
  <div class="services" style="left:630px; top:280px;">
    <div class="services__spacer"></div>
    <ul>
      <li>Cleaning Service</li>
      <li>Handyman Service</li>
    </ul>
  </div>

  <div class="accent-stripe"></div>
  <div class="reviews-band">
    <div class="reviews-band__text">Check out our <span class="reviews-band__stars">★★★★★</span><br>reviews at <span class="reviews-band__url">www.brellorhc.example</span></div>
    <div class="follow">Follow US On <span class="follow__icon"></span><span class="follow__icon"></span></div>
  </div>

  <div class="email-strip">
    <svg width="12" height="9" viewBox="0 0 12 9"><rect x="0.5" y="0.5" width="11" height="8" fill="var(--yellow)"/><path d="M0.5 0.5 L6 5 L11.5 0.5" stroke="var(--charcoal)" fill="none"/></svg>
    brellorhomecraftnyc@mailbox.example
  </div>

  <div class="call-block">
    <div class="call-block__text">
      <span class="call-block__label">Call Us</span>
      <span class="call-block__phone">555-014-2290</span>
    </div>
  </div>
</section>

<section class="flyer flyer--back">
  <svg class="hero-frame" viewBox="0 0 420 400" role="img" aria-label="Photo: black company service van with open side door parked on a driveway">
    <defs>
      <linearGradient id="photoBack" x1="0" y1="0" x2="1" y2="1">
        <stop offset="0" stop-color="var(--van-a)"/>
        <stop offset="1" stop-color="var(--van-b)"/>
      </linearGradient>
    </defs>
    <polygon points="105,0 315,0 420,200 315,400 105,400 0,200" fill="var(--red)"/>
    <polygon points="112,12 308,12 406,200 308,388 112,388 14,200" fill="var(--yellow)"/>
    <polygon points="116,18 304,18 399,200 304,382 116,382 21,200" fill="url(#photoBack)"/>
  </svg>

  <div class="logo">
    <span class="logo__mark"></span>
    <span class="logo__name">Brellor</span>
    <span class="logo__tag">HOMECRAFT SERVICES</span>
  </div>

  <h1 class="headline">
    <span class="headline__lead">Call the pros, not the cons</span>
    <span class="headline__main">We do it all, large and small</span>
  </h1>

  <div class="services" style="left:480px; top:140px;">
    <div class="services__title">Our Service</div>
    <ul>
      <li>Personal Advice for DIY</li>
      <li>Mount TV</li>
      <li>Carpentry</li>
      <li>General contractor</li>
      <li>Electrical services</li>
    </ul>
  </div>
  <div class="services" style="left:636px; top:140px;">
    <div class="services__spacer"></div>
    <ul>
      <li>Thermal inspections</li>
      <li>Install mailbox</li>
      <li>Painter</li>
      <li>Plumbing services</li>
      <li>Handyman services</li>
    </ul>
  </div>

  <svg class="estimate" viewBox="0 0 96 96" aria-hidden="true">
    <polygon points="28,3 68,3 93,28 93,68 68,93 28,93 3,68 3,28" fill="var(--white)" stroke="var(--red)" stroke-width="3"/>
  </svg>
  <div class="estimate"><span class="estimate__text">FREE<br>ESTIMATE</span></div>

  <div class="services" style="left:480px; top:256px;">
    <div class="services__title">New Offerings</div>
    <ul>
      <li>THERMAL INSPECTION</li>
      <li>CLEANING SERVICES</li>
    </ul>
  </div>

  <div class="accent-stripe"></div>
  <div class="reviews-band">
    <div class="reviews-band__text">Check out our <span class="reviews-band__stars">★★★★★</span><br>reviews at <span class="reviews-band__url">www.brellorhc.example</span></div>
    <div class="follow">Follow US On <span class="follow__icon"></span><span class="follow__icon"></span></div>
  </div>

  <div class="email-strip">
    <svg width="12" height="9" viewBox="0 0 12 9"><rect x="0.5" y="0.5" width="11" height="8" fill="var(--yellow)"/><path d="M0.5 0.5 L6 5 L11.5 0.5" stroke="var(--charcoal)" fill="none"/></svg>
    brellorhomecraftnyc@mailbox.example
  </div>

  <div class="call-block">
    <div class="call-block__text">
      <span class="call-block__label">Call Us</span>
      <span class="call-block__phone">555-014-2290</span>
    </div>
  </div>
</section>

</body>
</html>
```